Fast Money - Simple Book Cover Design

Hello,

I am in need of a cover for my new book. The Book Title Is

"Standing Growth - Keys to Glowing Customer Ratings That Fill The Calendar and Draw Fresh Clients Through Every Entrance!"

Author: Fireman Dale Orsworth

What I want: This is a book for businesses on improving their online reputation. I want to have 5 Stars on the cover. You can look at this quarvex search for ideas of what I am meaning.....

(copy and paste)

http://www.quarvex-find.example/search?q=5+star+online+reviews&mode=images&ref=kx7Lp2QwZt9 (copy and paste)

I am open to different color schemes for the book. I am partial to dark blues if you make it look good. Here is another book that I really like the cover of....

http://www.brindlemart.example/Clipwave-Tactics-Earning-Promotion-ebook/item/Z93KT4WQPX

I want the cover BOLD and to STAND OUT.

I am looking for a design to help establish me as an authority for online reputation marketing. This book will be both in Pagely format and be used in print as well.

I am open to questions....

Thanks!

Dale

Reason: I don't believe we have received the right designs. I am going to give everyone more time...

Reason: Hi everyone, I had some stuff come up and was not able to be involved in this project. I am extending because we have not seen the exact thing we want and need time to work with designers to get it right. Thanks Dale

Reason: I am currently traveling and can't wrap this up until I get back.

Target Market(s)

Business Owners

Industry/Entity Type

Business

Requirements
Must have
• Title and Subtitle

Author Name

5 Stars Images....
Nice to have
• Creativity

Bold and stand out

Professional

Should not have
• thin text, small to read text, lame graphics,

```html
<!DOCTYPE html>
<html lang="en">
<head>
<meta charset="utf-8">
<title>Standing Growth – Book Cover</title>
<link rel="stylesheet" href="https://fonts.googleapis.com/css2?family=Archivo+Black&display=swap">
<style>
  :root {
    --black: #000006;
    --navy-deep: #020726;
    --navy: #061a6e;
    --royal: #0b34c8;
    --electric: #2d5cff;
    --strand: #9fb6ff;
    --white: #ffffff;
    --gold-light: #fff47a;
    --gold: #f7c600;
    --gold-dark: #b87800;
  }
  html, body {
    margin: 0;
    padding: 0;
    width: 900px;
    height: 1200px;
    overflow: hidden;
    background: var(--black);
  }
  .cover {
    position: relative;
    width: 900px;
    height: 1200px;
    overflow: hidden;
    font-family: "Archivo Black", "Arial Black", sans-serif;
  }
  .cover__backdrop {
    position: absolute;
    inset: 0;
    background:
      radial-gradient(ellipse 34% 20% at 40% 78%, rgba(190,205,255,0.55), transparent 75%),
      radial-gradient(ellipse 48% 30% at 38% 80%, rgba(110,140,255,0.6), transparent 75%),
      radial-gradient(ellipse 16% 60% at 86% 30%, rgba(150,175,255,0.7), transparent 75%),
      radial-gradient(ellipse 26% 75% at 84% 45%, rgba(60,100,255,0.65), transparent 80%),
      radial-gradient(ellipse 40% 30% at 72% 92%, rgba(80,110,255,0.5), transparent 75%),
      radial-gradient(ellipse 70% 55% at 48% 80%, var(--royal), transparent 85%),
      radial-gradient(ellipse 75% 55% at 18% 18%, var(--black) 10%, transparent 80%),
      linear-gradient(165deg, var(--black) 0%, var(--navy-deep) 25%, var(--navy) 50%, #0a2aa0 75%, var(--navy-deep) 100%);
  }
  .cover__subtitle {
    position: absolute;
    top: 34px;
    left: 0;
    right: 0;
    margin: 0;
    text-align: center;
    color: var(--white);
    font-size: 30px;
    line-height: 46px;
    letter-spacing: 1.5px;
    text-transform: uppercase;
    font-weight: 400;
  }
  .cover__stars {
    position: absolute;
    top: 170px;
    left: 0;
    width: 900px;
    height: 250px;
  }
  .cover__title {
    position: absolute;
    top: 340px;
    left: 0;
    right: 0;
    margin: 0;
    text-align: center;
    text-transform: uppercase;
    font-size: 124px;
    line-height: 124px;
    letter-spacing: 4px;
    font-weight: 400;
  }
  .cover__title-line {
    display: block;
    background: linear-gradient(180deg, var(--gold-light) 0%, var(--gold) 45%, var(--gold-dark) 100%);
    -webkit-background-clip: text;
    background-clip: text;
    color: transparent;
    filter: drop-shadow(3px 4px 0 #5a3a00) drop-shadow(0 0 6px rgba(0,0,0,0.6));
  }
  .cover__author {
    position: absolute;
    top: 1090px;
    left: 0;
    right: 0;
    margin: 0;
    text-align: center;
    color: var(--white);
    font-size: 38px;
    line-height: 50px;
    letter-spacing: 1px;
    text-transform: uppercase;
    font-weight: 400;
    text-shadow: 0 2px 8px rgba(0,0,20,0.7);
  }
</style>
</head>
<body>
  <main class="cover">
    <div class="cover__backdrop" role="img" aria-label="Glowing blue fibre-optic light strands fanning up from the lower left and streaming down the right edge on a dark blue background"></div>

    <p class="cover__subtitle">
      Keys to Glowing Customer Ratings<br>
      That Fill the Calendar and Draw<br>
      Fresh Clients Through Every Entrance
    </p>

    <svg class="cover__stars" viewBox="0 0 900 250" aria-label="Five gold stars">
      <defs>
        <linearGradient id="facet-light" x1="0" y1="0" x2="0" y2="1">
          <stop offset="0" stop-color="#fff59a"/>
          <stop offset="1" stop-color="#f2c200"/>
        </linearGradient>
        <linearGradient id="facet-dark" x1="0" y1="0" x2="0" y2="1">
          <stop offset="0" stop-color="#d9a200"/>
          <stop offset="1" stop-color="#9a6500"/>
        </linearGradient>
        <linearGradient id="reflection-fade" x1="0" y1="0" x2="0" y2="1">
          <stop offset="0" stop-color="#fff" stop-opacity="0.45"/>
          <stop offset="0.6" stop-color="#fff" stop-opacity="0"/>
        </linearGradient>
        <mask id="reflection-mask" maskUnits="userSpaceOnUse" x="0" y="150" width="900" height="100">
          <rect x="0" y="150" width="900" height="100" fill="url(#reflection-fade)"/>
        </mask>
        <g id="star">
          <polygon points="0,-80 18.8,-25.9 0,0" fill="url(#facet-light)"/>
          <polygon points="0,-80 -18.8,-25.9 0,0" fill="url(#facet-dark)"/>
          <polygon points="76.1,-24.7 18.8,-25.9 0,0" fill="url(#facet-dark)"/>
          <polygon points="76.1,-24.7 30.4,9.9 0,0" fill="url(#facet-light)"/>
          <polygon points="47,64.7 30.4,9.9 0,0" fill="url(#facet-dark)"/>
          <polygon points="47,64.7 0,32 0,0" fill="url(#facet-light)"/>
          <polygon points="-47,64.7 0,32 0,0" fill="url(#facet-dark)"/>
          <polygon points="-47,64.7 -30.4,9.9 0,0" fill="url(#facet-light)"/>
          <polygon points="-76.1,-24.7 -30.4,9.9 0,0" fill="url(#facet-dark)"/>
          <polygon points="-76.1,-24.7 -18.8,-25.9 0,0" fill="url(#facet-light)"/>
        </g>
      </defs>

      <g class="stars-reflection" mask="url(#reflection-mask)">
        <use href="#star" transform="translate(120 230) scale(1 -0.6)"/>
        <use href="#star" transform="translate(285 230) scale(1 -0.6)"/>
        <use href="#star" transform="translate(450 230) scale(1 -0.6)"/>
        <use href="#star" transform="translate(615 230) scale(1 -0.6)"/>
        <use href="#star" transform="translate(779 230) scale(1 -0.6)"/>
      </g>

      <g class="stars-row">
        <use href="#star" transform="translate(120 86)"/>
        <use href="#star" transform="translate(285 86)"/>
        <use href="#star" transform="translate(450 86)"/>
        <use href="#star" transform="translate(615 86)"/>
        <use href="#star" transform="translate(779 86)"/>
      </g>
    </svg>

    <h1 class="cover__title">
      <span class="cover__title-line">Standing</span>
      <span class="cover__title-line">Growth</span>
    </h1>

    <p class="cover__author">Fireman Dale Orsworth</p>
  </main>
</body>
</html>
```